Website for Plumbing Company, Coastline Heating Co.

I need a 7-page fully HTML-coded website for my plumbing company, Coastline Heating Co.. We specialize in installation, repair, and replacement of both gas and electric water heaters. Although we offer both tankless (on-demand) water heaters and standard (with tank) water heaters, most of our business is related to standard (with tank) water heaters in the USA market.

These are the pages I need:
1. Home page with sections such as About Us, Our Services, Why Choose Us, Testimonials, Location Map (Palm Beach County Florida), Quote Request Form, Join Our Newsletter, Mission Statement, etc.

2. Gas Water Heaters

3. Electric Water Heaters

4. Tankless Water Heaters

5. About Us

6. Contact Us

7. Privacy Policy, Terms & Conditions

Be sure to mention the following points:
1. Same-Day Service
2. Best Price Guarantee
3. 100% Satisfaction Rating
4. 15-Year Warranty on Water Heater & Parts
5. Lifetime Warranty on Workmanship
*All Warranties are Transferrable Upon Home Sale

Once design is selected and finalized, I need the website coded in a standard HTML/CSS and temporarily hosted on your development server so I can see the website functionality that is not observable from screenshots, such as section animations, etc. Once those details are finalized, I will move the source code to my server and complete the project.

Target Market(s)

Residential Home Owners and Business Owners

Industry/Entity Type

Plumbing, Home Services, Remodeling, Construction

Coding

Coded - Design and coding required

Number of Pages Required

5+ page

Colors
0054AA
0677BA
7BADD7
CADEEF
E8F1F8
FFC000
F8CF3A
FAE287
FDF2CF
FEFAEE
EE7325
F08F49
F5BC92
FAE3D3
FDF4ED

Requirements
Must have
• Clean, colorful, and professional

```html
<!DOCTYPE html>
<html lang="en">
<head>
<meta charset="utf-8">
<title>Coastline Heating Co. – Website Page Set</title>
<link href="https://fonts.googleapis.com/css2?family=Poppins:wght@400;500;600;700;800&display=swap" rel="stylesheet">
<style>
:root{
  --board:#3a3a3a;
  --board-edge:#555;
  --navy:#0b1a3a;
  --navy-2:#12295a;
  --blue:#0054AA;
  --blue-2:#0677BA;
  --sky:#7BADD7;
  --mist:#CADEEF;
  --ice:#E8F1F8;
  --orange:#EE7325;
  --orange-2:#F08F49;
  --gold:#FFC000;
  --ink:#14213d;
  --muted:#5d6678;
  --line:#dfe6ef;
  --white:#fff;
}
*{box-sizing:border-box;margin:0;padding:0}
html,body{width:1200px;height:4680px;overflow:hidden}
body{background:var(--board);font-family:'Poppins',sans-serif;color:var(--ink);position:relative}
.board-frame{position:absolute;left:16px;top:16px;right:16px;bottom:16px;border:2px solid var(--board-edge)}
.icons{position:absolute;width:0;height:0}

.page{position:absolute;width:448px;background:var(--white);overflow:hidden;display:flex;flex-direction:column;box-shadow:0 6px 18px rgba(0,0,0,.35)}
.col-left{left:132px}
.col-right{left:620px}

/* hero + nav */
.hero{position:relative;flex:none;background:linear-gradient(90deg,var(--navy) 0%,var(--navy) 48%,var(--navy-2) 100%);color:var(--white);overflow:hidden}
.hero-photo{position:absolute;right:0;top:0;bottom:0;width:58%;background:linear-gradient(90deg,rgba(11,26,58,1) 0%,rgba(58,88,132,.85) 35%,#8fa9c8 70%,#c9d6e4 100%)}
.nav{position:relative;z-index:2;display:flex;align-items:center;gap:10px;height:26px;padding:0 14px;background:rgba(5,14,36,.55)}
.brand{display:flex;align-items:center;gap:4px;font-weight:700;font-size:7.5px;color:var(--white);white-space:nowrap}
.brand-dot{width:9px;height:9px;border-radius:50%;background:var(--orange)}
.nav-links{display:flex;gap:8px;margin-left:auto;font-size:5.4px;color:#d6e2f2}
.btn{display:inline-block;background:var(--orange);color:var(--white);font-weight:600;font-size:5.6px;padding:4px 8px;border-radius:2px;white-space:nowrap}
.btn-blue{background:var(--blue)}
.hero-body{position:relative;z-index:2;padding:0 22px}
.hero-home{height:230px}
.hero-home .hero-body{padding-top:56px}
.hero-inner{height:130px}
.hero-inner .hero-body{padding-top:54px}
.eyebrow{font-size:5.4px;color:var(--orange-2);font-weight:600;letter-spacing:.3px;text-transform:uppercase}
.hero h1{font-size:17px;line-height:1.2;font-weight:700;max-width:220px;margin:3px 0 6px}
.hero-inner h1{font-size:15px;max-width:230px}
.hero p{font-size:5.8px;color:#c5d3e6;max-width:190px;line-height:1.5;margin-bottom:8px}

/* sections */
.sec{flex:1 0 auto;display:flex;flex-direction:column;justify-content:center;padding:18px 22px}
.sec-tint{background:var(--ice)}
.sec-head{text-align:center;margin-bottom:12px}
.sec-head h2{font-size:13px;font-weight:700;color:var(--ink);line-height:1.3}
.sec-head p{font-size:5.8px;color:var(--muted);max-width:260px;margin:3px auto 0;line-height:1.5}
h3{font-size:12px;font-weight:700;color:var(--ink);margin-bottom:6px;line-height:1.3}
.txt{font-size:5.8px;color:var(--muted);line-height:1.6;margin-bottom:6px}
.photo{border-radius:4px}

/* about split */
.split{display:flex;gap:16px;align-items:center}
.split > *{flex:1}
.about-photo{height:160px;position:relative;background:linear-gradient(135deg,#c7d3e0,#8a9fb8 55%,#5d7596)}
.badge-years{position:absolute;left:8px;top:10px;background:var(--navy);color:var(--white);padding:6px 8px;border-radius:3px;font-size:5.4px;line-height:1.3}
.badge-years b{display:block;font-size:14px}
.checks{list-style:none;display:grid;gap:4px;margin:5px 0 8px}
.checks li{display:flex;align-items:center;gap:4px;font-size:5.8px;color:var(--ink)}
.checks svg{width:8px;height:8px;flex:none}

/* service cards */
.cards{display:grid;gap:8px}
.cards-4{grid-template-columns:repeat(4,1fr)}
.cards-3{grid-template-columns:repeat(3,1fr)}
.svc{background:var(--white);border:1px solid var(--line);border-radius:4px;overflow:hidden}
.svc-photo{height:72px;background:linear-gradient(160deg,#d9e2ec,#95a9c1 60%,#62799a)}
.cards-3 .svc-photo{height:92px}
.svc-body{padding:6px}
.svc-body h4{font-size:6.2px;font-weight:600;margin-bottom:3px;line-height:1.35}
.svc-body p{font-size:5.2px;color:var(--muted);line-height:1.5;margin-bottom:5px}
.svc-feature{background:var(--blue)}
.svc-feature h4,.svc-feature p{color:var(--white)}

/* why panel */
.why{display:flex;border-radius:6px;overflow:hidden;background:linear-gradient(120deg,var(--navy) 0%,var(--navy-2) 55%,var(--blue) 100%);color:var(--white);min-height:170px}
.why-text{flex:1.1;padding:18px}
.why-text h3{color:var(--white);font-size:12.5px}
.why-text .txt{color:#c7d5ea}
.why-grid{display:grid;grid-template-columns:1fr 1fr;gap:5px;margin:6px 0 9px}
.why-item{display:flex;align-items:center;gap:4px;background:rgba(255,255,255,.1);border-radius:3px;padding:5px 4px;font-size:5.4px}
.why-item svg{width:8px;height:8px;flex:none}
.why-photo{flex:.9;background:linear-gradient(180deg,#9fb2c9,#6d86a6 55%,#3c557c)}
.note{font-size:4.8px;color:#b9c9df}

/* map */
.map{height:160px;background:linear-gradient(135deg,#cfe6d4,#b7d5e6 55%,#a3c6df)}
.info-card{background:var(--white);border:1px solid var(--line);border-radius:4px;padding:12px;box-shadow:0 2px 6px rgba(11,26,58,.08)}
.info-row{display:flex;align-items:center;gap:5px;font-size:5.8px;margin-bottom:6px;color:var(--ink)}
.ico{width:12px;height:12px;border-radius:50%;background:var(--blue);display:flex;align-items:center;justify-content:center;flex:none}
.ico svg{width:7px;height:7px}
.cities{display:grid;grid-template-columns:1fr 1fr;gap:3px 8px;font-size:5.2px;color:var(--muted);margin:5px 0 9px}

/* testimonials */
.quotes{display:grid;grid-template-columns:repeat(3,1fr);gap:8px}
.quote{background:var(--white);border:1px solid var(--line);border-radius:4px;padding:10px}
.quote-feature{background:linear-gradient(160deg,var(--blue-2),var(--blue));color:var(--white);border:none}
.stars{color:var(--gold);font-size:7px;letter-spacing:1px;margin-bottom:5px}
.quote p{font-size:5.4px;line-height:1.6;color:var(--muted);margin-bottom:8px}
.quote-feature p{color:#e2ecf8}
.who{display:flex;align-items:center;gap:5px;font-size:5.4px;font-weight:600}
.avatar{width:13px;height:13px;border-radius:50%;background:linear-gradient(135deg,#d7c3b0,#8d7a68);flex:none}
.who span{display:block;font-weight:400;font-size:4.8px;opacity:.75}
.center-btn{text-align:center;margin-top:12px}

/* forms */
.form{display:grid;grid-template-columns:1fr 1fr;gap:7px}
.field{border:1px solid var(--line);background:var(--white);border-radius:2px;height:19px;font-size:5.4px;color:#9aa3b3;padding:0 6px;display:flex;align-items:center}
.field-wide{grid-column:1/-1}
.field-area{height:48px;align-items:flex-start;padding-top:5px}
.submit{grid-column:1/-1;background:linear-gradient(90deg,var(--blue),var(--blue-2));color:var(--white);font-size:6px;font-weight:600;text-align:center;height:18px;display:flex;align-items:center;justify-content:center;border-radius:2px}
.form-card{background:var(--white);border:1px solid var(--line);border-radius:4px;padding:14px}
.form-card h3{text-align:center}

/* CTA */
.cta{background:linear-gradient(100deg,var(--blue) 0%,var(--blue-2) 100%);border-radius:6px;color:var(--white);text-align:center;padding:22px 24px}
.cta h3{color:var(--white);font-size:12.5px;max-width:240px;margin:0 auto 5px}
.cta .txt{color:#d8e6f6}

/* stats + team */
.stats{display:grid;grid-template-columns:repeat(4,1fr);gap:6px;margin-top:10px}
.stat{background:var(--navy);color:var(--white);text-align:center;border-radius:3px;padding:6px 2px;font-size:5px}
.stat b{display:block;font-size:10px;color:var(--gold)}
.team{display:grid;grid-template-columns:repeat(4,1fr);gap:6px}
.member-photo{height:92px;background:linear-gradient(180deg,#dfe6ee,#9fb0c6)}
.member{font-size:5.4px;font-weight:600;background:var(--navy);color:var(--white);padding:5px;border-radius:0 0 3px 3px}
.member span{display:block;font-weight:400;font-size:4.8px;opacity:.8}

/* contact cards */
.c-cards{display:grid;grid-template-columns:repeat(3,1fr);gap:8px}
.c-card{background:var(--white);border:1px solid var(--line);border-radius:4px;padding:12px 6px;text-align:center;font-size:5.2px;color:var(--muted)}
.c-card .ico{margin:0 auto 5px;width:15px;height:15px}
.c-card b{display:block;color:var(--ink);font-size:6.2px;margin-bottom:2px}

/* policy */
.policy{border:1px solid var(--line);border-radius:4px;padding:16px;background:var(--white)}
.policy h4{font-size:8px;font-weight:700;margin:10px 0 6px}
.policy h4:first-child{margin-top:0}
.acc{display:flex;justify-content:space-between;align-items:center;border:1px solid var(--line);border-radius:2px;padding:7px 8px;margin-bottom:6px;font-size:6px}
.acc svg{width:7px;height:7px}

/* footer */
.footer{flex:none;background:var(--navy);color:#bccbe0;padding:20px 22px 9px}
.footer-cols{display:grid;grid-template-columns:1.4fr 1fr 1fr 1.3fr;gap:12px}
.footer h5{color:var(--white);font-size:6.2px;font-weight:600;margin-bottom:4px}
.footer ul{list-style:none;font-size:5.2px;line-height:1.8}
.footer p{font-size:5.2px;line-height:1.6;margin-top:4px}
.footer .brand{font-size:8px}
.footer-bottom{border-top:1px solid rgba(255,255,255,.12);margin-top:12px;padding-top:7px;font-size:4.8px;text-align:center;color:#8ea0bd}
</style>
</head>
<body>
<div class="board-frame"></div>

<svg class="icons" aria-hidden="true">
  <symbol id="tick" viewBox="0 0 10 10"><circle cx="5" cy="5" r="5" fill="#EE7325"/><path d="M2.8 5.2l1.5 1.5 3-3.2" stroke="#fff" stroke-width="1.2" fill="none"/></symbol>
  <symbol id="phone" viewBox="0 0 10 10"><path d="M2.5 1.2l1.6 1.8-.8 1.2c.6 1.2 1.4 2 2.5 2.5l1.2-.8 1.8 1.6-1 1.2C4.6 8.6 1.4 5.4 1.3 2.2z" fill="#fff"/></symbol>
  <symbol id="pin" viewBox="0 0 10 10"><path d="M5 .8a3 3 0 0 1 3 3c0 2.3-3 5.6-3 5.6S2 6.1 2 3.8a3 3 0 0 1 3-3z" fill="#fff"/><circle cx="5" cy="3.8" r="1.1" fill="#0054AA"/></symbol>
  <symbol id="mail" viewBox="0 0 10 10"><rect x="1" y="2.2" width="8" height="5.6" rx=".6" fill="#fff"/><path d="M1.3 2.6L5 5.6l3.7-3" stroke="#0054AA" stroke-width=".8" fill="none"/></symbol>
  <symbol id="clock" viewBox="0 0 10 10"><circle cx="5" cy="5" r="3.8" fill="none" stroke="#fff" stroke-width="1"/><path d="M5 2.9V5l1.5 1" stroke="#fff" stroke-width="1" fill="none"/></symbol>
  <symbol id="chev" viewBox="0 0 10 10"><path d="M2.5 3.8L5 6.3l2.5-2.5" stroke="#0054AA" stroke-width="1.3" fill="none"/></symbol>
</svg>

<!-- ================= HOME ================= -->
<section class="page col-left" style="top:120px;height:1700px">
  <header class="hero hero-home">
    <div class="hero-photo" role="img" aria-label="Technician in blue uniform standing beside installed water heaters"></div>
    <nav class="nav"><div class="brand"><span class="brand-dot"></span>Coastline Heating Co.</div><div class="nav-links"><span>Home</span><span>Gas</span><span>Electric</span><span>Tankless</span><span>About</span><span>Contact</span></div><span class="btn">Get A Free Quote</span></nav>
    <div class="hero-body">
      <div class="eyebrow">Same-Day Service · Palm Beach County</div>
      <h1>Reliable Water Heater Services in Palm Beach County</h1>
      <p>Installation, repair and replacement of gas, electric and tankless water heaters, backed by a best price guarantee.</p>
      <span class="btn">Request Service</span>
    </div>
  </header>

  <div class="sec">
    <div class="split">
      <div class="about-photo photo" role="img" aria-label="Plumber checking a tank water heater in a utility room"><div class="badge-years"><b>15+</b>Years Of<br>Experience</div></div>
      <div>
        <div class="eyebrow">Who We Are</div>
        <h3>About Coastline Heating Co.</h3>
        <p class="txt">We are a local plumbing team focused on standard tank water heaters for homes and businesses, with tankless options when they fit your needs.</p>
        <ul class="checks">
          <li><svg><use href="#tick"/></svg>15-Year Warranty on Water Heater &amp; Parts</li>
          <li><svg><use href="#tick"/></svg>Lifetime Warranty on Workmanship</li>
          <li><svg><use href="#tick"/></svg>100% Satisfaction Rating</li>
        </ul>
        <span class="btn btn-blue">Learn More</span>
      </div>
    </div>
  </div>

  <div class="sec sec-tint">
    <div class="sec-head"><div class="eyebrow">What We Do</div><h2>Our Services</h2></div>
    <div class="cards cards-4">
      <div class="svc"><div class="svc-photo" role="img" aria-label="Gas water heater installation"></div><div class="svc-body"><h4>Gas Water Heater Installation</h4><p>Safe venting and gas line hookup by licensed pros.</p><span class="btn">Read More</span></div></div>
      <div class="svc svc-feature"><div class="svc-photo" role="img" aria-label="Electric water heater repair"></div><div class="svc-body"><h4>Electric Water Heater Repair</h4><p>Elements, thermostats and wiring fixed fast.</p><span class="btn">Read More</span></div></div>
      <div class="svc"><div class="svc-photo" role="img" aria-label="Tankless water heater on a wall"></div><div class="svc-body"><h4>Tankless Water Heater Service</h4><p>On-demand units sized and set up right.</p><span class="btn">Read More</span></div></div>
      <div class="svc"><div class="svc-photo" role="img" aria-label="Old tank water heater being replaced"></div><div class="svc-body"><h4>Emergency Water Heater Replacement</h4><p>Same-day swap when your tank fails.</p><span class="btn">Read More</span></div></div>
    </div>
  </div>

  <div class="sec">
    <div class="why">
      <div class="why-text">
        <h3>Why Choose Coastline Heating Co.?</h3>
        <p class="txt">Honest pricing, clean work and warranties that protect your home.</p>
        <div class="why-grid">
          <div class="why-item"><svg><use href="#tick"/></svg>Same-Day Service</div>
          <div class="why-item"><svg><use href="#tick"/></svg>Best Price Guarantee</div>
          <div class="why-item"><svg><use href="#tick"/></svg>100% Satisfaction</div>
          <div class="why-item"><svg><use href="#tick"/></svg>15-Year Warranty</div>
          <div class="why-item"><svg><use href="#tick"/></svg>Lifetime Workmanship</div>
          <div class="why-item"><svg><use href="#tick"/></svg>Licensed &amp; Insured</div>
        </div>
        <span class="btn">Get Started</span>
        <p class="note" style="margin-top:6px">*All warranties are transferable upon home sale</p>
      </div>
      <div class="why-photo" role="img" aria-label="Technician servicing a water heater"></div>
    </div>
  </div>

  <div class="sec sec-tint">
    <div class="sec-head"><h2>Serving Palm Beach County</h2></div>
    <div class="split">
      <div class="map photo" role="img" aria-label="Map of Palm Beach County, Florida"></div>
      <div class="info-card">
        <h3 style="font-size:8px">Our Service Area</h3>
        <div class="cities"><span>West Palm Beach</span><span>Boca Raton</span><span>Delray Beach</span><span>Jupiter</span><span>Boynton Beach</span><span>Wellington</span><span>Lake Worth</span><span>Palm Beach Gardens</span></div>
        <div class="info-row"><span class="ico"><svg><use href="#phone"/></svg></span>(561) 555-0148</div>
        <div class="info-row"><span class="ico"><svg><use href="#clock"/></svg></span>Mon–Sat · 7am – 7pm</div>
        <span class="btn">Book Same-Day Service</span>
      </div>
    </div>
  </div>

  <div class="sec">
    <div class="sec-head"><h2>What Our Customers Say</h2></div>
    <div class="quotes">
      <div class="quote"><div class="stars">★★★★★</div><p>Our tank failed in the morning and a new one was running by dinner. Fair price and tidy work.</p><div class="who"><span class="avatar" role="img" aria-label="Customer portrait"></span><div>Laura M.<span>Boca Raton</span></div></div></div>
      <div class="quote quote-feature"><div class="stars">★★★★★</div><p>They beat two other quotes and explained every step. The warranty gave us real peace of mind.</p><div class="who"><span class="avatar" role="img" aria-label="Customer portrait"></span><div>Daniel R.<span>Jupiter</span></div></div></div>
      <div class="quote"><div class="stars">★★★★★</div><p>Friendly crew, on time and very clean. We now have hot water for the whole family again.</p><div class="who"><span class="avatar" role="img" aria-label="Customer portrait"></span><div>Priya K.<span>Wellington</span></div></div></div>
    </div>
    <div class="center-btn"><span class="btn">View All Reviews</span></div>
  </div>

  <div class="sec sec-tint">
    <div class="split">
      <div>
        <h3>Request A Free Quote</h3>
        <p class="txt">Tell us about your water heater and we will reply within the hour.</p>
        <div class="info-row"><span class="ico"><svg><use href="#phone"/></svg></span>(561) 555-0148</div>
        <div class="info-row"><span class="ico"><svg><use href="#mail"/></svg></span>hello@coastlineheating.com</div>
        <div class="info-row"><span class="ico"><svg><use href="#pin"/></svg></span>1200 Harbor Lane, West Palm Beach, FL</div>
      </div>
      <div class="form">
        <div class="field">First Name</div><div class="field">Last Name</div>
        <div class="field">Email</div><div class="field">Phone</div>
        <div class="field field-wide">Service Needed</div>
        <div class="field field-wide field-area">Message</div>
        <div class="submit">Get My Free Quote</div>
      </div>
    </div>
  </div>

  <footer class="footer">
    <div class="footer-cols">
      <div><div class="brand"><span class="brand-dot"></span>Coastline Heating Co.</div><p>Water heater installation, repair and replacement across Palm Beach County.</p></div>
      <div><h5>Quick Links</h5><ul><li>Home</li><li>About Us</li><li>Contact</li><li>Privacy Policy</li></ul></div>
      <div><h5>Services</h5><ul><li>Gas Water Heaters</li><li>Electric Water Heaters</li><li>Tankless Water Heaters</li></ul></div>
      <div><h5>Contact Us</h5><ul><li>(561) 555-0148</li><li>hello@coastlineheating.com</li><li>West Palm Beach, FL</li></ul></div>
    </div>
    <div class="footer-bottom">© 2024 Coastline Heating Co. All rights reserved.</div>
  </footer>
</section>

<!-- ================= TANKLESS ================= -->
<section class="page col-left" style="top:1880px;height:1128px">
  <header class="hero hero-inner">
    <div class="hero-photo" role="img" aria-label="Technician next to a wall-mounted tankless unit"></div>
    <nav class="nav"><div class="brand"><span class="brand-dot"></span>Coastline Heating Co.</div><div class="nav-links"><span>Home</span><span>Gas</span><span>Electric</span><span>Tankless</span><span>About</span><span>Contact</span></div><span class="btn">Get A Free Quote</span></nav>
    <div class="hero-body"><div class="eyebrow">Home / Tankless</div><h1>Tankless Water Heaters</h1></div>
  </header>
  <div class="sec">
    <div class="sec-head"><h2>Tankless Water<br>Heater Services</h2></div>
    <div class="cards cards-3">
      <div class="svc"><div class="svc-photo" role="img" aria-label="Tankless heater installation"></div><div class="svc-body"><h4>Tankless Installation</h4><p>Endless hot water sized to your home.</p></div></div>
      <div class="svc svc-feature"><div class="svc-photo" role="img" aria-label="Tankless heater repair"></div><div class="svc-body"><h4>Tankless Repair</h4><p>Error codes and flow issues solved.</p></div></div>
      <div class="svc"><div class="svc-photo" role="img" aria-label="Tankless descaling service"></div><div class="svc-body"><h4>Descaling &amp; Flush</h4><p>Yearly care that keeps units efficient.</p></div></div>
    </div>
  </div>
  <div class="sec sec-tint">
    <div class="why">
      <div class="why-text">
        <h3>Why Choose Tankless Water Heaters?</h3>
        <p class="txt">Heat water only when you need it and free up floor space.</p>
        <div class="why-grid">
          <div class="why-item"><svg><use href="#tick"/></svg>Endless Hot Water</div>
          <div class="why-item"><svg><use href="#tick"/></svg>Lower Energy Bills</div>
          <div class="why-item"><svg><use href="#tick"/></svg>Compact Design</div>
          <div class="why-item"><svg><use href="#tick"/></svg>Longer Lifespan</div>
        </div>
        <span class="btn">Get A Quote</span>
      </div>
      <div class="why-photo" role="img" aria-label="Technician adjusting a tankless heater"></div>
    </div>
  </div>
  <div class="sec">
    <div class="sec-head"><h2>What Our Customers Say</h2></div>
    <div class="quotes">
      <div class="quote"><div class="stars">★★★★★</div><p>The switch to tankless cut our bill and the install was spotless.</p><div class="who"><span class="avatar" role="img" aria-label="Customer portrait"></span><div>Mark T.<span>Delray Beach</span></div></div></div>
      <div class="quote quote-feature"><div class="stars">★★★★★</div><p>Clear advice on sizing and a great price. Showers never run cold now.</p><div class="who"><span class="avatar" role="img" aria-label="Customer portrait"></span><div>Anna P.<span>Jupiter</span></div></div></div>
      <div class="quote"><div class="stars">★★★★★</div><p>Quick service and a team that really knows tankless systems.</p><div class="who"><span class="avatar" role="img" aria-label="Customer portrait"></span><div>Chris L.<span>Lake Worth</span></div></div></div>
    </div>
  </div>
  <div class="sec">
    <div class="cta"><h3>Ready For Expert Gas Water Heater Service?</h3><p class="txt">Same-day appointments with a best price guarantee.</p><span class="btn">Call (561) 555-0148</span></div>
  </div>
  <footer class="footer">
    <div class="footer-cols">
      <div><div class="brand"><span class="brand-dot"></span>Coastline Heating Co.</div><p>Water heater experts in Palm Beach County.</p></div>
      <div><h5>Quick Links</h5><ul><li>Home</li><li>About Us</li><li>Contact</li></ul></div>
      <div><h5>Services</h5><ul><li>Gas</li><li>Electric</li><li>Tankless</li></ul></div>
      <div><h5>Contact Us</h5><ul><li>(561) 555-0148</li><li>hello@coastlineheating.com</li></ul></div>
    </div>
    <div class="footer-bottom">© 2024 Coastline Heating Co. All rights reserved.</div>
  </footer>
</section>

<!-- ================= CONTACT ================= -->
<section class="page col-left" style="top:3072px;height:840px">
  <header class="hero hero-inner">
    <div class="hero-photo" role="img" aria-label="Technician holding a phone beside a water heater"></div>
    <nav class="nav"><div class="brand"><span class="brand-dot"></span>Coastline Heating Co.</div><div class="nav-links"><span>Home</span><span>Gas</span><span>Electric</span><span>Tankless</span><span>About</span><span>Contact</span></div><span class="btn">Get A Free Quote</span></nav>
    <div class="hero-body"><div class="eyebrow">Home / Contact</div><h1>Contact Coastline Heating Co. Today</h1></div>
  </header>
  <div class="sec">
    <div class="c-cards">
      <div class="c-card"><span class="ico"><svg><use href="#phone"/></svg></span><b>Call Us</b>(561) 555-0148</div>
      <div class="c-card"><span class="ico"><svg><use href="#mail"/></svg></span><b>Email Us</b>hello@coastlineheating.com</div>
      <div class="c-card"><span class="ico"><svg><use href="#clock"/></svg></span><b>Business Hours</b>Mon–Sat 7am – 7pm</div>
    </div>
  </div>
  <div class="sec sec-tint">
    <div class="sec-head"><h2>Serving Palm Beach County</h2></div>
    <div class="split">
      <div class="map photo" role="img" aria-label="Map of Palm Beach County, Florida"></div>
      <div class="info-card">
        <div class="cities"><span>West Palm Beach</span><span>Boca Raton</span><span>Delray Beach</span><span>Jupiter</span><span>Boynton Beach</span><span>Wellington</span></div>
        <div class="info-row"><span class="ico"><svg><use href="#pin"/></svg></span>1200 Harbor Lane, West Palm Beach</div>
        <div class="info-row"><span class="ico"><svg><use href="#phone"/></svg></span>(561) 555-0148</div>
        <span class="btn">Get Directions</span>
      </div>
    </div>
  </div>
  <div class="sec">
    <div class="form-card">
      <h3>Send Us A Message</h3>
      <div class="form">
        <div class="field">Full Name</div><div class="field">Email Address</div>
        <div class="field">Phone Number</div><div class="field">Service Type</div>
        <div class="field field-wide field-area">Your Message</div>
        <div class="submit">Send Message</div>
      </div>
    </div>
  </div>
  <footer class="footer">
    <div class="footer-cols">
      <div><div class="brand"><span class="brand-dot"></span>Coastline Heating Co.</div><p>Water heater experts in Palm Beach County.</p></div>
      <div><h5>Quick Links</h5><ul><li>Home</li><li>About Us</li><li>Contact</li></ul></div>
      <div><h5>Services</h5><ul><li>Gas</li><li>Electric</li><li>Tankless</li></ul></div>
      <div><h5>Contact Us</h5><ul><li>(561) 555-0148</li><li>hello@coastlineheating.com</li></ul></div>
    </div>
    <div class="footer-bottom">© 2024 Coastline Heating Co. All rights reserved.</div>
  </footer>
</section>

<!-- ================= GAS ================= -->
<section class="page col-right" style="top:120px;height:1160px">
  <header class="hero hero-inner">
    <div class="hero-photo" role="img" aria-label="Technician beside a gas water heater"></div>
    <nav class="nav"><div class="brand"><span class="brand-dot"></span>Coastline Heating Co.</div><div class="nav-links"><span>Home</span><span>Gas</span><span>Electric</span><span>Tankless</span><span>About</span><span>Contact</span></div><span class="btn">Get A Free Quote</span></nav>
    <div class="hero-body"><div class="eyebrow">Home / Gas</div><h1>Gas Water Heaters</h1></div>
  </header>
  <div class="sec">
    <div class="sec-head"><h2>Our Gas Water<br>Heater Services</h2></div>
    <div class="cards cards-3">
      <div class="svc"><div class="svc-photo" role="img" aria-label="Gas heater installation"></div><div class="svc-body"><h4>Gas Installation</h4><p>Code-compliant venting and gas hookup.</p></div></div>
      <div class="svc svc-feature"><div class="svc-photo" role="img" aria-label="Gas heater repair"></div><div class="svc-body"><h4>Gas Repair</h4><p>Pilot, burner and valve issues fixed.</p></div></div>
      <div class="svc"><div class="svc-photo" role="img" aria-label="Gas heater replacement"></div><div class="svc-body"><h4>Gas Replacement</h4><p>Same-day swap of worn-out tanks.</p></div></div>
    </div>
  </div>
  <div class="sec sec-tint">
    <div class="why">
      <div class="why-text">
        <h3>Why Choose Gas Water Heaters?</h3>
        <p class="txt">Fast recovery and lower running costs for busy homes.</p>
        <div class="why-grid">
          <div class="why-item"><svg><use href="#tick"/></svg>Fast Heating</div>
          <div class="why-item"><svg><use href="#tick"/></svg>Lower Running Cost</div>
          <div class="why-item"><svg><use href="#tick"/></svg>Works In Outages</div>
          <div class="why-item"><svg><use href="#tick"/></svg>High Capacity</div>
        </div>
        <span class="btn">Get A Quote</span>
      </div>
      <div class="why-photo" role="img" aria-label="Gas water heater in a garage"></div>
    </div>
  </div>
  <div class="sec">
    <div class="sec-head"><h2>What Our Customers Say</h2></div>
    <div class="quotes">
      <div class="quote"><div class="stars">★★★★★</div><p>New gas heater installed the same day we called. Excellent service.</p><div class="who"><span class="avatar" role="img" aria-label="Customer portrait"></span><div>Sam W.<span>Boynton Beach</span></div></div></div>
      <div class="quote quote-feature"><div class="stars">★★★★★</div><p>Fair quote, safe install and they hauled the old tank away.</p><div class="who"><span class="avatar" role="img" aria-label="Customer portrait"></span><div>Rosa G.<span>Wellington</span></div></div></div>
      <div class="quote"><div class="stars">★★★★★</div><p>Professional from start to finish. Highly recommended.</p><div class="who"><span class="avatar" role="img" aria-label="Customer portrait"></span><div>Tom B.<span>Jupiter</span></div></div></div>
    </div>
    <div class="center-btn"><span class="btn">Book Your Service</span></div>
  </div>
  <div class="sec">
    <div class="cta"><h3>Ready For Expert Gas Water Heater Service?</h3><p class="txt">Same-day appointments with a best price guarantee.</p><span class="btn">Call (561) 555-0148</span></div>
  </div>
  <footer class="footer">
    <div class="footer-cols">
      <div><div class="brand"><span class="brand-dot"></span>Coastline Heating Co.</div><p>Water heater experts in Palm Beach County.</p></div>
      <div><h5>Quick Links</h5><ul><li>Home</li><li>About Us</li><li>Contact</li></ul></div>
      <div><h5>Services</h5><ul><li>Gas</li><li>Electric</li><li>Tankless</li></ul></div>
      <div><h5>Contact Us</h5><ul><li>(561) 555-0148</li><li>hello@coastlineheating.com</li></ul></div>
    </div>
    <div class="footer-bottom">© 2024 Coastline Heating Co. All rights reserved.</div>
  </footer>
</section>

<!-- ================= ELECTRIC ================= -->
<section class="page col-right" style="top:1328px;height:1152px">
  <header class="hero hero-inner">
    <div class="hero-photo" role="img" aria-label="Technician beside an electric water heater"></div>
    <nav class="nav"><div class="brand"><span class="brand-dot"></span>Coastline Heating Co.</div><div class="nav-links"><span>Home</span><span>Gas</span><span>Electric</span><span>Tankless</span><span>About</span><span>Contact</span></div><span class="btn">Get A Free Quote</span></nav>
    <div class="hero-body"><div class="eyebrow">Home / Electric</div><h1>Electric Water Heaters</h1></div>
  </header>
  <div class="sec">
    <div class="sec-head"><h2>Electric Water Heater<br>Services</h2></div>
    <div class="cards cards-3">
      <div class="svc"><div class="svc-photo" role="img" aria-label="Electric heater installation"></div><div class="svc-body"><h4>Electric Installation</h4><p>Correct wiring and breaker sizing.</p></div></div>
      <div class="svc svc-feature"><div class="svc-photo" role="img" aria-label="Electric heater element repair"></div><div class="svc-body"><h4>Element Repair</h4><p>Heating elements and thermostats.</p></div></div>
      <div class="svc"><div class="svc-photo" role="img" aria-label="Electric heater replacement"></div><div class="svc-body"><h4>Electric Replacement</h4><p>Efficient new tanks installed fast.</p></div></div>
    </div>
  </div>
  <div class="sec sec-tint">
    <div class="why">
      <div class="why-text">
        <h3>Why Choose Electric Water Heaters?</h3>
        <p class="txt">Simple, safe and easy to install in almost any home.</p>
        <div class="why-grid">
          <div class="why-item"><svg><use href="#tick"/></svg>No Gas Line Needed</div>
          <div class="why-item"><svg><use href="#tick"/></svg>Low Upfront Cost</div>
          <div class="why-item"><svg><use href="#tick"/></svg>Quiet Operation</div>
          <div class="why-item"><svg><use href="#tick"/></svg>Easy Upkeep</div>
        </div>
        <span class="btn">Get A Quote</span>
      </div>
      <div class="why-photo" role="img" aria-label="Technician testing an electric water heater"></div>
    </div>
  </div>
  <div class="sec">
    <div class="sec-head"><h2>What Our Customers Say</h2></div>
    <div class="quotes">
      <div class="quote"><div class="stars">★★★★★</div><p>They found the bad element in minutes. Hot water back by noon.</p><div class="who"><span class="avatar" role="img" aria-label="Customer portrait"></span><div>Nina F.<span>Boca Raton</span></div></div></div>
      <div class="quote quote-feature"><div class="stars">★★★★★</div><p>Great price on a new electric tank and a warranty we trust.</p><div class="who"><span class="avatar" role="img" aria-label="Customer portrait"></span><div>Joe D.<span>Delray Beach</span></div></div></div>
      <div class="quote"><div class="stars">★★★★★</div><p>Courteous, on time and left everything clean.</p><div class="who"><span class="avatar" role="img" aria-label="Customer portrait"></span><div>Kim H.<span>Lake Worth</span></div></div></div>
    </div>
  </div>
  <div class="sec">
    <div class="cta"><h3>Ready For Expert Gas Water Heater Service?</h3><p class="txt">Same-day appointments with a best price guarantee.</p><span class="btn">Call (561) 555-0148</span></div>
  </div>
  <footer class="footer">
    <div class="footer-cols">
      <div><div class="brand"><span class="brand-dot"></span>Coastline Heating Co.</div><p>Water heater experts in Palm Beach County.</p></div>
      <div><h5>Quick Links</h5><ul><li>Home</li><li>About Us</li><li>Contact</li></ul></div>
      <div><h5>Services</h5><ul><li>Gas</li><li>Electric</li><li>Tankless</li></ul></div>
      <div><h5>Contact Us</h5><ul><li>(561) 555-0148</li><li>hello@coastlineheating.com</li></ul></div>
    </div>
    <div class="footer-bottom">© 2024 Coastline Heating Co. All rights reserved.</div>
  </footer>
</section>

<!-- ================= ABOUT ================= -->
<section class="page col-right" style="top:2520px;height:1160px">
  <header class="hero hero-inner">
    <div class="hero-photo" role="img" aria-label="Technician with arms crossed in front of water heaters"></div>
    <nav class="nav"><div class="brand"><span class="brand-dot"></span>Coastline Heating Co.</div><div class="nav-links"><span>Home</span><span>Gas</span><span>Electric</span><span>Tankless</span><span>About</span><span>Contact</span></div><span class="btn">Get A Free Quote</span></nav>
    <div class="hero-body"><div class="eyebrow">Home / About</div><h1>About Us</h1></div>
  </header>
  <div class="sec">
    <div class="split">
      <div class="about-photo photo" role="img" aria-label="Service van and team at a customer home"></div>
      <div>
        <h3>About Coastline Heating Co.</h3>
        <p class="txt">A family-run plumbing company serving Palm Beach County with water heater installs, repairs and replacements.</p>
        <ul class="checks">
          <li><svg><use href="#tick"/></svg>Same-Day Service</li>
          <li><svg><use href="#tick"/></svg>Best Price Guarantee</li>
          <li><svg><use href="#tick"/></svg>Transferable Warranties</li>
        </ul>
      </div>
    </div>
  </div>
  <div class="sec sec-tint">
    <div class="split">
      <div>
        <h3>Our Story</h3>
        <p class="txt">We started with one truck and a promise to treat every home like our own. Today our licensed crew handles hundreds of water heaters each year, mostly standard tank models.</p>
        <p class="txt">Every job comes with a 15-year warranty on heater and parts and a lifetime warranty on workmanship.</p>
      </div>
      <div class="about-photo photo" style="height:120px" role="img" aria-label="Plumber working on pipes"></div>
    </div>
    <div class="stats">
      <div class="stat"><b>15+</b>Years</div>
      <div class="stat"><b>5,000+</b>Installs</div>
      <div class="stat"><b>100%</b>Satisfaction</div>
      <div class="stat"><b>24h</b>Response</div>
    </div>
  </div>
  <div class="sec">
    <div class="split">
      <div class="about-photo photo" style="height:120px" role="img" aria-label="Technician inspecting a water heater"></div>
      <div>
        <h3>Our Mission</h3>
        <p class="txt">To deliver reliable hot water fast, at a fair price, with work that lasts and warranties that follow your home.</p>
        <span class="btn btn-blue">Contact Us</span>
      </div>
    </div>
  </div>
  <div class="sec sec-tint">
    <div class="sec-head"><h2>Meet The Team</h2></div>
    <div class="team">
      <div><div class="member-photo" role="img" aria-label="Team member portrait"></div><div class="member">James Carter<span>Founder</span></div></div>
      <div><div class="member-photo" role="img" aria-label="Team member portrait"></div><div class="member">Luis Romero<span>Lead Plumber</span></div></div>
      <div><div class="member-photo" role="img" aria-label="Team member portrait"></div><div class="member">Erin Walsh<span>Office Manager</span></div></div>
      <div><div class="member-photo" role="img" aria-label="Team member portrait"></div><div class="member">Ray Jensen<span>Technician</span></div></div>
    </div>
  </div>
  <footer class="footer">
    <div class="footer-cols">
      <div><div class="brand"><span class="brand-dot"></span>Coastline Heating Co.</div><p>Water heater experts in Palm Beach County.</p></div>
      <div><h5>Quick Links</h5><ul><li>Home</li><li>About Us</li><li>Contact</li></ul></div>
      <div><h5>Services</h5><ul><li>Gas</li><li>Electric</li><li>Tankless</li></ul></div>
      <div><h5>Contact Us</h5><ul><li>(561) 555-0148</li><li>hello@coastlineheating.com</li></ul></div>
    </div>
    <div class="footer-bottom">© 2024 Coastline Heating Co. All rights reserved.</div>
  </footer>
</section>

<!-- ================= PRIVACY ================= -->
<section class="page col-right" style="top:3728px;height:832px">
  <header class="hero hero-inner">
    <div class="hero-photo" role="img" aria-label="Technician standing beside a water heater"></div>
    <nav class="nav"><div class="brand"><span class="brand-dot"></span>Coastline Heating Co.</div><div class="nav-links"><span>Home</span><span>Gas</span><span>Electric</span><span>Tankless</span><span>About</span><span>Contact</span></div><span class="btn">Get A Free Quote</span></nav>
    <div class="hero-body"><div class="eyebrow">Home / Legal</div><h1>Privacy Policy &amp; Terms</h1></div>
  </header>
  <div class="sec">
    <div class="policy">
      <h4>Privacy Policy</h4>
      <div class="acc">Information We Collect<svg><use href="#chev"/></svg></div>
      <div class="acc">How We Use Your Data<svg><use href="#chev"/></svg></div>
      <div class="acc">Data Protection<svg><use href="#chev"/></svg></div>
      <div class="acc">Your Rights<svg><use href="#chev"/></svg></div>
      <h4>Terms &amp; Conditions</h4>
      <div class="acc">Service Agreement<svg><use href="#chev"/></svg></div>
      <div class="acc">Payments &amp; Pricing<svg><use href="#chev"/></svg></div>
      <div class="acc">Liability<svg><use href="#chev"/></svg></div>
      <h4>Warranty Information</h4>
      <div class="acc">15-Year Heater &amp; Parts Warranty<svg><use href="#chev"/></svg></div>
      <div class="acc">Lifetime Workmanship Warranty<svg><use href="#chev"/></svg></div>
      <div class="acc">Transfer Upon Home Sale<svg><use href="#chev"/></svg></div>
    </div>
  </div>
  <footer class="footer">
    <div class="footer-cols">
      <div><div class="brand"><span class="brand-dot"></span>Coastline Heating Co.</div><p>Water heater experts in Palm Beach County.</p></div>
      <div><h5>Quick Links</h5><ul><li>Home</li><li>About Us</li><li>Contact</li></ul></div>
      <div><h5>Services</h5><ul><li>Gas</li><li>Electric</li><li>Tankless</li></ul></div>
      <div><h5>Contact Us</h5><ul><li>(561) 555-0148</li><li>hello@coastlineheating.com</li></ul></div>
    </div>
    <div class="footer-bottom">© 2024 Coastline Heating Co. All rights reserved.</div>
  </footer>
</section>
</body>
</html>
```